Small boutique multi-family apartment developer needs premium website design.

We are a growing real estate development company specializing in multi family apartment development. Our company Mireval Stone Development focuses on passive real estate investors looking to maximize their current real estate portfolio by allowing us to develop and reposition their current properties allowing them more cashflow while we are also able to take over the management of their asset in order to ensure optimal performance on a consistent basis.

```html
<!DOCTYPE html>
<html lang="en">
<head>
<meta charset="utf-8">
<title>Mireval Stone Development – Website &amp; Identity</title>
<link rel="stylesheet" href="https://fonts.googleapis.com/css2?family=Alegreya+Sans:wght@400;500;700&family=Arimo:wght@400;700&family=Roboto+Condensed:wght@400;700&display=swap">
<style>
:root{
  --navy:#0b1a3c;
  --navy-deep:#061a3f;
  --navy-mid:#12325f;
  --gold:#e2c26a;
  --gold-dark:#d4b055;
  --gold-foot:#e4b95b;
  --bg:#e3e4e6;
  --paper:#e6e7e9;
  --white:#ffffff;
  --ink:#0b1a3c;
}
*{margin:0;padding:0;box-sizing:border-box}
html,body{width:774px;height:1200px;overflow:hidden;background:var(--bg)}
body{font-family:"Alegreya Sans",sans-serif;color:var(--ink)}
.canvas{position:relative;width:774px;height:1200px;overflow:hidden;background:var(--bg)}
.abs{position:absolute}
.photo{position:absolute}

/* website page */
.page{position:absolute;left:0;top:0;width:249px;height:1200px;background:var(--paper);box-shadow:3px 0 6px rgba(0,0,0,.25);overflow:hidden}
.nav{position:absolute;left:0;top:0;width:249px;height:21px;background:var(--navy)}
.nav-brand{position:absolute;left:8px;top:9px;display:flex;align-items:center;gap:2px;color:var(--gold);font-size:3.2px;font-weight:500;white-space:nowrap}
.nav-brand .dot{width:6px;height:6px;border-radius:50%;background:var(--gold)}
.nav-links{position:absolute;left:72px;top:10px;display:flex;gap:4px;font-size:3px;color:#c9cfdb;white-space:nowrap}
.nav-links .active{color:var(--gold)}
.btn-gold{position:absolute;background:var(--gold);color:var(--navy);font-size:2px;letter-spacing:.2px;display:flex;align-items:center;justify-content:center;border-radius:1.5px;font-family:"Arimo",sans-serif;white-space:nowrap}

.hero-photo{position:absolute;left:0;top:21px;width:186px;height:109px;background:linear-gradient(135deg,#8aa0b3,#7d7457 45%,#4d6a3a)}
.hero-title{position:absolute;right:12px;top:67px;text-align:right;font-size:7px;line-height:10px;letter-spacing:.4px;font-weight:500}
.hero-sub{position:absolute;right:12px;top:109px;text-align:right;font-size:4px;line-height:5.3px;letter-spacing:.3px}

.strip{position:absolute;left:38px;top:140px;width:166px;height:37px;background:var(--gold);border-radius:6px;box-shadow:0 2px 3px rgba(0,0,0,.2)}
.strip-item{position:absolute;top:0;width:38px;height:37px;display:flex;flex-direction:column;align-items:center;justify-content:center;gap:3px;font-size:2.2px;color:var(--navy);white-space:nowrap}
.strip-active{position:absolute;left:124px;top:134px;width:35px;height:47px;background:var(--navy);border-radius:4px;display:flex;flex-direction:column;align-items:center;justify-content:center;gap:4px;font-size:2.2px;color:var(--gold)}
.arrow-faint{position:absolute;top:156px;font-size:5px;color:var(--gold)}

.section-title{position:absolute;left:0;width:249px;text-align:center;font-size:5.6px;letter-spacing:.5px;font-weight:500}
.frame{position:absolute;border:.6px solid var(--navy)}
.text-box{position:absolute;background:var(--navy);color:#dfe3ea;border-radius:1.5px;padding:6px 4px 4px;overflow:hidden}
.text-box h4{font-weight:400;font-size:3.5px;letter-spacing:.3px;margin-bottom:3px;color:var(--white)}
.text-box p{font-size:2.2px;line-height:2.6px;text-align:justify}

.svc-lead{position:absolute;left:39px;top:335px;width:76px;font-size:4.6px;line-height:7.4px;font-weight:500}
.svc{position:absolute;width:36px;height:38px;border-radius:1.5px;display:flex;flex-direction:column;align-items:center;justify-content:center;gap:4px;font-size:2px;line-height:2.4px;text-align:center;box-shadow:0 1px 2px rgba(0,0,0,.25)}
.svc-navy{background:var(--navy);color:#d6dbe4}
.svc-gold{background:var(--gold);color:var(--navy)}

.projects{position:absolute;left:0;top:574px;width:249px;height:106px;display:flex}
.project{flex:1;position:relative}
.project-label{position:absolute;left:10px;bottom:4px;transform:rotate(-90deg);transform-origin:left bottom;font-size:2px;color:#e7d59a;white-space:nowrap}
.zoom{position:absolute;left:82px;top:617px;width:25px;height:25px;border-radius:50%;background:rgba(226,194,106,.85);display:flex;align-items:center;justify-content:center}
.slide-nav{position:absolute;top:629px;font-size:2.2px;color:#e7d59a;font-family:"Arimo",sans-serif;white-space:nowrap}

.tcard{position:absolute;border-radius:2px;box-shadow:0 1.5px 3px rgba(0,0,0,.35);font-family:"Roboto Condensed",sans-serif;text-align:center;padding:6px 3px 2px;overflow:hidden}
.tcard-navy{background:linear-gradient(180deg,#1d3563,#14284f);color:#d6dbe4}
.tcard-gold{background:var(--gold);color:var(--navy)}
.tcard h5{font-size:3.8px;line-height:4.6px;font-weight:700}
.tcard-navy h5{color:#f0f2f6}
.stars{color:#f2c53c;font-size:5px;letter-spacing:.2px;margin:1px 0}
.tcard p{font-size:2.9px;line-height:3.6px}

.years{position:absolute;left:0;top:844px;width:249px;height:78px;background:linear-gradient(180deg,#c9a85e 0%,#a98a45 45%,#6f5a30 100%)}
.years-num{position:absolute;left:10px;top:846px;font-size:52px;line-height:60px;font-weight:700;color:rgba(240,240,240,.9);letter-spacing:-3px}
.years-text{position:absolute;left:23px;top:896px;font-size:5px;line-height:6px;color:var(--white);letter-spacing:.7px;font-weight:500;white-space:nowrap}
.play{position:absolute;left:186px;top:893px;width:10px;height:10px;border-radius:50%;background:#1d1d1d;display:flex;align-items:center;justify-content:center}
.play-text{position:absolute;left:198px;top:895px;font-size:3.2px;color:var(--white);letter-spacing:.5px;white-space:nowrap}
.play-line{position:absolute;left:196px;top:902px;width:53px;height:.5px;background:var(--white)}

.clients-title{letter-spacing:.8px}
.client{position:absolute;transform:translateX(-50%);display:flex;align-items:center;gap:2px;color:var(--gold-dark);font-size:5px;font-weight:500;white-space:nowrap}
.client .sq{width:5px;height:5px;background:var(--gold-dark)}

.contact{position:absolute;left:0;top:1026px;width:249px;height:82px;background:var(--navy)}
.contact-title{position:absolute;left:0;top:1037px;width:254px;text-align:center;font-family:"Arimo",sans-serif;font-size:6px;letter-spacing:.6px;color:#e6e9ef;font-weight:400}
.contact-title span{color:var(--gold)}
.contact-info{position:absolute;left:16px;top:1062px;font-family:"Arimo",sans-serif;font-size:2.8px;line-height:5.5px;color:#e6e9ef;white-space:nowrap}
.field{position:absolute;background:#152955;color:#dfe3ea;font-family:"Arimo",sans-serif;font-size:2.8px;padding:2.6px 3px;border-radius:.6px}
.pill{position:absolute;left:106px;top:1020px;width:36px;height:9px;border-radius:2.5px;background:var(--gold);color:var(--navy);font-family:"Arimo",sans-serif;font-size:2.8px;display:flex;align-items:center;justify-content:center;letter-spacing:.3px;white-space:nowrap}

.footer{position:absolute;left:0;top:1108px;width:249px;height:92px;background:var(--gold-foot)}
.footer-logo{position:absolute;left:111px;top:1105px;width:29px;height:37px;background:var(--navy);border:.7px solid #b08b36;display:flex;align-items:center;justify-content:center;gap:1.5px;color:var(--gold);font-size:2.4px;line-height:2.8px;padding:0 2px}
.footer-logo .dot{width:4px;height:4px;border-radius:50%;background:var(--gold);flex:none}
.footer-contact{position:absolute;left:10px;top:1145px;font-family:"Arimo",sans-serif;font-size:2.8px;line-height:7.6px;color:var(--navy);white-space:nowrap}
.footer-hours{position:absolute;left:106px;top:1160px;width:40px;text-align:center;font-family:"Arimo",sans-serif;font-size:2.8px;line-height:3.4px;color:var(--navy)}
.footer-col{position:absolute;top:1145px;font-family:"Arimo",sans-serif;font-size:2.8px;line-height:11.3px;color:var(--navy);white-space:nowrap}
.social{position:absolute;top:1182px;width:6px;height:6px;border-radius:50%;background:var(--white)}

/* identity board */
.board{position:absolute;left:273px;top:398px;width:469px;height:425px;border:1px solid var(--navy)}
.mark{position:absolute;left:391px;top:470px;width:200px;display:flex;flex-direction:column;align-items:center;gap:8px;color:var(--gold-dark);font-size:17px;font-weight:500;text-align:center;line-height:20px}
.mark .sq{width:26px;height:26px;background:linear-gradient(135deg,#ead27c,#d4b055);border-radius:3px}
.logo-card{position:absolute;top:587px;height:96px;border-radius:20px;box-shadow:2px 3px 4px rgba(0,0,0,.35);display:flex;align-items:center;justify-content:center;gap:4px;text-align:center;font-weight:500}
.logo-card .dot{width:12px;height:12px;border-radius:50%;flex:none}
.card-navy{left:305px;width:126px;background:var(--navy-deep);color:var(--gold);flex-direction:column;font-size:9px}
.card-navy .dot{background:var(--gold);width:16px;height:16px}
.card-light{left:445px;width:129px;background:#e9eaec;color:var(--navy-mid);font-size:7.6px;white-space:nowrap}
.card-light .dot{background:var(--gold)}
.card-gold{left:588px;width:130px;background:linear-gradient(90deg,#ebd57e,#d7b458);color:var(--navy-deep);font-size:10.5px;line-height:13px;text-align:left;gap:7px}
.card-gold .dot{background:var(--navy-deep);width:24px;height:24px}
.swatch{position:absolute;top:731px;width:84px;height:47px}
</style>
</head>
<body>
<div class="canvas">

  <section class="page">

    <header class="nav">
      <div class="nav-brand"><span class="dot"></span>Mireval Stone Development</div>
      <nav class="nav-links">
        <span class="active">HomePage</span><span>About Us</span><span>Services</span><span>Portfolio</span><span>Testimonials</span><span>Contact Us</span>
      </nav>
      <div class="btn-gold" style="left:213px;top:8.5px;width:27px;height:7.5px">BOOKING ONLINE</div>
    </header>

    <div class="hero-photo" role="img" aria-label="Photo of a smiling family with a dog receiving keys from an agent in front of apartment buildings"></div>
    <h1 class="hero-title">Boutique<br>Multifamily<br>Apartment<br>Development</h1>
    <p class="hero-sub">Expert Development<br>&amp; Management</p>

    <span class="arrow-faint" style="left:28px">&larr;</span>
    <span class="arrow-faint" style="left:209px">&rarr;</span>
    <div class="strip">
      <div class="strip-item" style="left:8px">
        <svg width="13" height="13" viewBox="0 0 13 13" fill="none" stroke="#0b1a3c" stroke-width=".6"><rect x="2" y="4" width="5" height="8"/><rect x="7" y="7" width="4" height="5"/><path d="M1 2 H12 M4 2 V4"/></svg>
        Multifamily Development</div>
      <div class="strip-item" style="left:45px">
        <svg width="13" height="13" viewBox="0 0 13 13" fill="none" stroke="#0b1a3c" stroke-width=".6"><rect x="1" y="9" width="2.5" height="3"/><rect x="5" y="7" width="2.5" height="5"/><rect x="9" y="4" width="2.5" height="8"/><path d="M1 7 L6 4 L11 1 M9 1 H11 V3"/></svg>
        Investment Growth</div>
      <div class="strip-item" style="left:127px">
        <svg width="13" height="13" viewBox="0 0 13 13" fill="none" stroke="#0b1a3c" stroke-width=".6"><path d="M1 7 L6.5 2 L12 7 M3 6 V12 H10 V6"/><rect x="5.5" y="8" width="2" height="4"/></svg>
        Property Repositioning</div>
    </div>
    <div class="strip-active">
      <svg width="13" height="13" viewBox="0 0 13 13" fill="none" stroke="#e2c26a" stroke-width=".6"><circle cx="5" cy="4" r="2"/><path d="M1.5 11 C1.5 8 3 7 5 7 C7 7 8.5 8 8.5 11"/><rect x="8" y="6" width="4" height="5"/></svg>
      Asset Management</div>

    <h2 class="section-title" style="top:201px">About Us</h2>
    <div class="frame" style="left:45px;top:239px;width:79px;height:56px"></div>
    <div class="photo" role="img" aria-label="Photo of business people reviewing an apartment building scale model" style="left:117px;top:215px;width:77px;height:69px;background:linear-gradient(135deg,#5a6f86,#8b8f86 50%,#3e4b40)"></div>
    <div class="text-box" style="left:51px;top:243px;width:67px;height:47px">
      <h4>Lorem Ipsum</h4>
      <p>Lorem ipsum dolor sit amet, consectetur adipiscing elit, sed do eiusmod tempor incididunt ut labore et dolore magna aliqua. Ut enim ad minim veniam, quis nostrud exercitation ullamco laboris nisi ut aliquip ex ea commodo consequat. Duis aute irure dolor in reprehenderit in voluptate velit esse cillum dolore eu fugiat nulla pariatur</p>
    </div>

    <h2 class="section-title" style="top:312px;left:-10px">Services</h2>
    <p class="svc-lead">Explore Real Estate Investments Through Expert Development and Management</p>
    <div class="btn-gold" style="left:38px;top:361px;width:28px;height:7.5px">BOOKING ONLINE</div>

    <div class="svc svc-navy" style="left:129px;top:333px">
      <svg width="12" height="12" viewBox="0 0 12 12" fill="none" stroke="#e2c26a" stroke-width=".6"><rect x="2" y="2" width="8" height="9"/><path d="M4 4 H5 M7 4 H8 M4 6 H5 M7 6 H8 M5 11 V9 H7 V11"/></svg>
      Multifamily<br>Apartment Development</div>
    <div class="svc svc-gold" style="left:175px;top:333px">
      <svg width="12" height="12" viewBox="0 0 12 12" fill="#0b1a3c"><rect x="1" y="4" width="4" height="8"/><rect x="5.5" y="1" width="4" height="11"/><rect x="10" y="6" width="1.5" height="6"/></svg>
      Property<br>Repositioning &amp;<br>Renovation</div>
    <div class="svc svc-navy" style="left:38px;top:373px">
      <svg width="12" height="12" viewBox="0 0 12 12" fill="none" stroke="#e2c26a" stroke-width=".6"><path d="M1 5 L6 1.5 L11 5 M2 4.5 V11 H10 V4.5"/><rect x="4" y="6" width="1.5" height="1.5"/><rect x="6.5" y="6" width="1.5" height="1.5"/></svg>
      Asset Management<br>&amp; Optimization</div>
    <div class="svc svc-navy" style="left:84px;top:373px">
      <svg width="12" height="12" viewBox="0 0 12 12" fill="none" stroke="#e2c26a" stroke-width=".6"><path d="M1 6 L5 3 L9 6 M2 5.5 V11 H8 V5.5"/><circle cx="9.5" cy="8.5" r="2"/><path d="M8.7 8.5 L9.3 9.1 L10.3 8"/></svg>
      Investment Portfolio<br>Maximization</div>
    <div class="svc svc-navy" style="left:129px;top:373px">
      <svg width="12" height="12" viewBox="0 0 12 12" fill="none" stroke="#e2c26a" stroke-width=".6"><rect x="1.5" y="2" width="5" height="9"/><rect x="6.5" y="5" width="4" height="6"/><path d="M3 4 H5 M3 6 H5 M3 8 H5 M8 7 H9 M8 9 H9"/></svg>
      Turnkey Development<br>Solutions</div>
    <div class="svc svc-navy" style="left:175px;top:373px">
      <svg width="12" height="12" viewBox="0 0 12 12" fill="none" stroke="#e2c26a" stroke-width=".6"><rect x="4" y="1" width="4" height="5"/><path d="M1 8 C3 7 5 7 7 8 L10 7 V10 L6 11 L1 10"/></svg>
      Custom<br>Development<br>Plans</div>

    <h2 class="section-title" style="top:438px;left:-6px">Why Choose Us</h2>
    <div class="photo" role="img" aria-label="Photo of a team with hard hat reviewing plans next to a house model" style="left:56px;top:451px;width:77px;height:69px;background:linear-gradient(135deg,#9fb0c0,#d8d4cc 55%,#7a7f84)"></div>
    <div class="frame" style="left:127px;top:480px;width:79px;height:57px"></div>
    <div class="text-box" style="left:133px;top:484px;width:67px;height:47px">
      <h4>Lorem Ipsum</h4>
      <p>Lorem ipsum dolor sit amet, consectetur adipiscing elit, sed do eiusmod tempor incididunt ut labore et dolore magna aliqua. Ut enim ad minim veniam, quis nostrud exercitation ullamco laboris nisi ut aliquip ex ea commodo consequat. Duis aute irure dolor in reprehenderit in voluptate velit esse cillum dolore eu fugiat nulla pariatur</p>
    </div>

    <h2 class="section-title" style="top:557px;left:-1px">Featured Projects &amp; Portfolio</h2>
    <div class="projects">
      <div class="project" role="img" aria-label="Photo of a modern mid-rise apartment building with a lawn" style="background:linear-gradient(180deg,#3c5475,#51606b 60%,#4f5a4a)"><span class="project-label">Urban Development</span></div>
      <div class="project" role="img" aria-label="Photo of a tall residential tower under a blue sky" style="background:linear-gradient(180deg,#7ea2c8,#c9d1d8 45%,#6c7d8a)"></div>
      <div class="project" role="img" aria-label="Photo of a white high-rise apartment facade" style="background:linear-gradient(180deg,#2e4169,#5c6c86 60%,#3a4863)"><span class="project-label">Luxury Residences</span></div>
      <div class="project" role="img" aria-label="Photo of apartment towers at dusk with trees" style="background:linear-gradient(180deg,#3a475a,#4b5650 60%,#2c3a2f)"><span class="project-label">Project Showcase</span></div>
    </div>
    <div class="zoom">
      <svg width="8" height="8" viewBox="0 0 8 8" fill="none" stroke="#fff" stroke-width=".5"><path d="M1 3 V1 H3 M5 1 H7 V3 M7 5 V7 H5 M3 7 H1 V5 M1 1 L3 3 M7 1 L5 3 M7 7 L5 5 M1 7 L3 5"/></svg>
    </div>
    <span class="slide-nav" style="left:8px">&larr; PREV</span>
    <span class="slide-nav" style="left:226px">NEXT &rarr;</span>

    <h2 class="section-title" style="top:701px;left:-3px">Testimonials</h2>
    <div class="tcard tcard-navy" style="left:-30px;top:743px;width:57px;height:74px;text-align:right">
      <h5>Nora T., Real<br>Estate Investor</h5><div class="stars">★★★</div>
      <p>development has been a game-changer for my portfolio. Their expertise in repositioning properties has significantly increased my cash flow and management services ensure my investments are performing at their best. I couldn't be happier with the results!</p>
    </div>
    <div class="tcard tcard-navy" style="left:32px;top:743px;width:57px;height:74px">
      <h5>Laura K.,<br>Property Owner</h5><div class="stars">★★★★★</div>
      <p>I partnered with Mireval Stone Development to revitalize an aging apartment complex, and the transformation has been remarkable. Their attention to detail and commitment to quality is evident in every aspect of the project. My tenants are thrilled with the upgrades, and so am I.</p>
    </div>
    <div class="tcard tcard-gold" style="left:94px;top:722px;width:58px;height:75px">
      <h5>Daniel P., Real<br>Estate Investor</h5><div class="stars">★★★★★</div>
      <p>Mireval Stone Development has been a game-changer for my portfolio. Their expertise in repositioning properties has significantly increased my cash flow, and their management services ensure my investments are always performing at their best. I couldn't be happier with the results!</p>
    </div>
    <div class="tcard tcard-navy" style="left:157px;top:743px;width:57px;height:74px">
      <h5>Victor H.,<br>Passive Investor</h5><div class="stars">★★★★★</div>
      <p>As a passive investor, I wanted a team I could trust to handle every aspect of development and management. Mireval Stone Development has exceeded my expectations. Their transparency, professionalism and results have made them an invaluable partner in my investment journey.</p>
    </div>
    <div class="tcard tcard-navy" style="left:219px;top:743px;width:57px;height:74px;text-align:left">
      <h5>Nora S.,<br>Multifamily<br>Developer</h5><div class="stars">★★★★★</div>
      <p>Mireval Stone has been a game-changer for my portfolio. Their repositioning significantly increased my cash flow, and their services ensure my investments are always performing at their best. I couldn't be happier with the results!</p>
    </div>

    <div class="years" role="img" aria-label="Photo of a furnished rooftop terrace overlooking a city skyline at golden hour"></div>
    <div class="years-num">20</div>
    <div class="years-text">YEARS OF SUCCESSFUL WORK<br>IN MARKET</div>
    <div class="play"><svg width="4" height="4" viewBox="0 0 4 4"><path d="M1 .5 L3.5 2 L1 3.5 Z" fill="#e2c26a"/></svg></div>
    <div class="play-text">PLAY THE VIDEO</div>
    <div class="play-line"></div>

    <h2 class="section-title clients-title" style="top:940px;left:2px">OUR CLIENTS</h2>
    <div class="client" style="left:32px;top:967px"><span class="sq"></span>Harborline</div>
    <div class="client" style="left:92px;top:967px">Venlo</div>
    <div class="client" style="left:153px;top:967px"><span class="sq"></span>Ashgrove Homes</div>
    <div class="client" style="left:207px;top:967px">Crestmoor</div>
    <div class="client" style="left:34px;top:996px"><span class="sq"></span>Tallis</div>
    <div class="client" style="left:92px;top:996px">Crestmoor</div>
    <div class="client" style="left:153px;top:996px">Venlo</div>
    <div class="client" style="left:210px;top:996px"><span class="sq"></span>Harborline</div>

    <div class="contact"></div>
    <div class="pill">WORK TOGETHER</div>
    <h2 class="contact-title">GET <span>IN TOUCH</span></h2>
    <div class="contact-info">
      +1 555 014 2290<br>+1 555 014 7781<br>hello@mirevalstone.dev<br>88 Harrow Lane, Suite 210 United States
    </div>
    <div class="field" style="left:107px;top:1058px;width:35px;height:10px">NAME</div>
    <div class="field" style="left:107px;top:1072px;width:35px;height:10px">EMAIL</div>
    <div class="field" style="left:150px;top:1058px;width:35px;height:10px">PHONE</div>
    <div class="field" style="left:150px;top:1072px;width:35px;height:10px">COMPANY</div>
    <div class="field" style="left:193px;top:1058px;width:50px;height:37px">MESSAGE</div>

    <footer class="footer"></footer>
    <div class="footer-logo"><span class="dot"></span><span>Mireval Stone Development</span></div>
    <div class="footer-contact">
      Contact<br>Lindell Road, 14 - City (Country)<br>(+555) 010 020 030<br>office@mirevalstone.dev
    </div>
    <div class="footer-hours">Open Everyday<br>From 7 AM to 8 PM</div>
    <div class="footer-col" style="left:172px">Home<br>News<br>Menu<br>Blog</div>
    <div class="footer-col" style="left:201px">Privacy Policy<br>Cookies<br>Conditions<br>Map Site</div>
    <span class="social" style="left:11px"></span>
    <span class="social" style="left:20px"></span>
    <span class="social" style="left:30px"></span>
    <span class="social" style="left:39px"></span>
  </section>

  <div class="board"></div>
  <div class="mark"><span class="sq"></span>Mireval Stone Development</div>

  <div class="logo-card card-navy"><span class="dot"></span>Mireval Stone Development</div>
  <div class="logo-card card-light"><span class="dot"></span>Mireval Stone Development</div>
  <div class="logo-card card-gold"><span class="dot"></span><span>Mireval Stone<br>Development</span></div>

  <div class="swatch" style="left:354px;background:var(--navy-mid)"></div>
  <div class="swatch" style="left:453px;background:linear-gradient(90deg,#ebd57e,#d7b458)"></div>
  <div class="swatch" style="left:555px;background:var(--navy-deep)"></div>

</div>
</body>
</html>
```